Harborline Security and Surveillance Business Card

Business Card Design - Company Name:Freedom Security and SurveillanceWe are a Security Systems Integrator Specializing in Security Systems/ Video Surveillance and Access Control. Our areas of expertise are:Security SystemsVideo SurveillanceAccess ControlFire Alarm SystemsNetwork CablingCellular BoostersMy input is the Front of the Card is: logo, name of Business, My Name, Phone Number, and email.Rear of Card is the 6 areas of expertise, I just dont want the front to be very busy.
Name: Dale Rowntree
Title: President
Email: dale@harborlinesecsys.example
website: harborlinesecsys.example

```html
<!DOCTYPE html>
<html lang="en">
<head>
<meta charset="utf-8">
<title>Harborline Security and Surveillance Business Card</title>
<link href="https://fonts.googleapis.com/css2?family=Oswald:wght@500&family=Roboto:wght@400;500&display=swap" rel="stylesheet">
<style>
  :root{
    --page:#d9d9db;
    --card:#141414;
    --card-edge:#262626;
    --blue:#0a5cc2;
    --silver:#c9cacc;
    --grey:#5e5e5e;
    --white:#f2f2f2;
  }
  *{margin:0;padding:0;box-sizing:border-box}
  html,body{width:1200px;height:1200px;overflow:hidden;background:var(--page);font-family:"Roboto",Arial,sans-serif}
  .sheet{position:relative;width:1200px;height:1200px}
  .card{position:absolute;left:150px;width:900px;height:514px;border-radius:34px;
    background:linear-gradient(135deg,#0b0b0b 0%,var(--card) 50%,var(--card-edge) 100%);overflow:hidden}
  .card--back{top:70px}
  .card--front{top:616px}

  .brand{display:flex;align-items:center;gap:14px;color:var(--blue);font-weight:500;text-transform:uppercase;letter-spacing:.22em}
  .brand__mark{width:22px;height:22px;border-radius:50%;background:var(--blue);flex:none}
  .brand__name{font-size:26px;line-height:1.25}
  .brand__name small{display:block;font-size:13px;letter-spacing:.45em}

  .card--back .brand{position:absolute;top:70px;left:0;right:0;justify-content:center}
  .card--back .brand__name{text-align:center}

  .services{position:absolute;left:60px;right:60px;top:230px;display:flex;justify-content:space-between;list-style:none}
  .service{width:140px;text-align:center;color:var(--white);font-size:16px;line-height:1.2}
  .service svg{display:block;margin:0 auto 10px;width:96px;height:96px}

  .card--front .brand{position:absolute;top:64px;left:56px}
  .person{position:absolute;left:56px;top:220px}
  .person__name{font-family:"Oswald","Arial Narrow",sans-serif;font-weight:500;font-size:52px;line-height:1;text-transform:uppercase;letter-spacing:-.01em}
  .person__first{color:var(--silver)}
  .person__last{color:var(--blue)}
  .person__title{color:var(--grey);font-size:22px;margin-top:2px}
  .person__rule{width:56px;height:5px;background:var(--blue);margin-top:18px}
  .contact{position:absolute;left:56px;top:356px;list-style:none;color:var(--silver);font-size:21px}
  .contact li{display:flex;align-items:center;gap:14px;margin-bottom:14px}
  .contact svg{width:22px;height:22px;flex:none}
  .contact .accent{color:var(--blue)}

  .emblem{position:absolute;right:60px;top:70px;width:380px;height:380px;border-radius:50%;
    background:radial-gradient(circle at 40% 35%,#1b6fd6 0%,var(--blue) 60%,#08479a 100%)}
</style>
</head>
<body>
<main class="sheet">

  <section class="card card--back" aria-label="Card back">
    <div class="brand">
      <span class="brand__mark"></span>
      <p class="brand__name">Harborline Security<small>and surveillance</small></p>
    </div>

    <ul class="services">
      <li class="service">
        <svg viewBox="0 0 96 96" fill="none" stroke="var(--blue)" stroke-width="2.5"><circle cx="48" cy="48" r="45"/><rect x="24" y="34" width="40" height="14" rx="2" fill="var(--blue)" transform="rotate(-12 44 41)"/><path d="M52 50v10h12"/><rect x="64" y="54" width="6" height="12" fill="var(--blue)"/></svg>
        Video<br>Surveillance
      </li>
      <li class="service">
        <svg viewBox="0 0 96 96" fill="none" stroke="var(--blue)" stroke-width="2.5"><circle cx="48" cy="48" r="45"/><rect x="28" y="24" width="30" height="44" rx="3" fill="var(--blue)"/><rect x="33" y="29" width="20" height="8" fill="#111"/><g fill="#111" stroke="none"><circle cx="35" cy="44" r="2"/><circle cx="43" cy="44" r="2"/><circle cx="51" cy="44" r="2"/><circle cx="35" cy="52" r="2"/><circle cx="43" cy="52" r="2"/><circle cx="51" cy="52" r="2"/></g><rect x="50" y="50" width="22" height="18" rx="2" fill="var(--blue)" stroke="#111"/></svg>
        Access Control
      </li>
      <li class="service">
        <svg viewBox="0 0 96 96" fill="none" stroke="var(--blue)" stroke-width="2.5"><circle cx="48" cy="48" r="45"/><circle cx="48" cy="42" r="12"/><circle cx="48" cy="42" r="5" fill="var(--blue)"/><path d="M30 28a24 24 0 0 0 0 28M66 28a24 24 0 0 1 0 28M24 22a32 32 0 0 0 0 40M72 22a32 32 0 0 1 0 40"/><path d="M44 72c-4-4 0-8 4-12 2 4 6 6 4 10-2 4-6 4-8 2z" fill="var(--blue)"/></svg>
        Fire Alarm<br>Systems
      </li>
      <li class="service">
        <svg viewBox="0 0 96 96" fill="none" stroke="var(--blue)" stroke-width="2.5"><circle cx="48" cy="48" r="45"/><path d="M28 62c-6 4 2 10 10 4l14-12"/><rect x="52" y="28" width="14" height="22" rx="2" fill="var(--blue)" transform="rotate(40 59 39)"/><path d="M40 70l20-4"/></svg>
        Network Cabling
      </li>
      <li class="service">
        <svg viewBox="0 0 96 96" fill="none" stroke="var(--blue)" stroke-width="2.5"><circle cx="48" cy="48" r="45"/><circle cx="48" cy="36" r="5" fill="var(--blue)"/><path d="M48 41l-12 34M48 41l12 34M40 62h16M38 26a14 14 0 0 0 0 20M58 26a14 14 0 0 1 0 20M32 20a22 22 0 0 0 0 32M64 20a22 22 0 0 1 0 32"/></svg>
        Cellular<br>Boosters
      </li>
    </ul>
  </section>

  <section class="card card--front" aria-label="Card front">
    <div class="brand">
      <span class="brand__mark"></span>
      <p class="brand__name">Harborline Security<small>and surveillance</small></p>
    </div>

    <div class="person">
      <h1 class="person__name"><span class="person__first">Dale</span> <span class="person__last">Rowntree</span></h1>
      <p class="person__title">President</p>
      <div class="person__rule"></div>
    </div>

    <ul class="contact">
      <li>
        <svg viewBox="0 0 24 24" fill="none" stroke="var(--blue)" stroke-width="2"><rect x="2" y="5" width="20" height="14" rx="1"/><path d="M2 6l10 7 10-7"/></svg>
        dale@harborlinesecsys.example
      </li>
      <li>
        <svg viewBox="0 0 24 24" fill="none" stroke="var(--blue)" stroke-width="1.8"><circle cx="12" cy="12" r="10"/><ellipse cx="12" cy="12" rx="4" ry="10"/><path d="M2 12h20M4 7h16M4 17h16"/></svg>
        <span>www.<span class="accent">harborlinesecsys</span>.example</span>
      </li>
    </ul>

    <div class="emblem" role="img" aria-label="Large brand emblem area"></div>
  </section>

</main>
</body>
</html>
```